'Velunor' Nutritional supplements label design (UPDATED)

- 'Velunor' is a upscale health supplements brand
-The company will be packing the products in plastic bottles like other supplements
-Try to use a distinct design which is recognizable from distance
-Brand Logo is attached

-UPDATE- 2-

Label Dimensions and Design:

Hi Everyone,

Sorry for the late response caused by some very busy schedule.

Anyhow, here are the dimensions of the label (Self Adhesive) that we need:

Length of Label : 18cm
Height of Label : 6.5 cm

Product Names:

-Metabolism Formula
-Complete Multivitamins and Minerals (For Men, Women and Kids)
-Healthy Bones
-Skin Support
-Omega-3 oil for Healthy Heart

As for the ingredients just use Lorem Ipsum for now.

Many thanks to all of you in advance.

Target Market(s)

Middle Income families

Industry/Entity Type

Plastic

Requirements
Must have
• -Quality
-Effective
-Unique

```html
<!DOCTYPE html>
<html lang="en">
<head>
<meta charset="utf-8">
<title>Velunor – Multivitamins &amp; Minerals Label</title>
<link rel="stylesheet" href="https://fonts.googleapis.com/css2?family=Roboto+Condensed:wght@400;700&family=Roboto:wght@400;500;700&display=swap">
<style>
  :root {
    --orange: #ef6748;
    --grey-text: #8c8c8c;
    --blue: #1b8fcb;
    --teal: #16b39c;
    --green: #1f9a3a;
    --ink: #1c1c1c;
    --panel-sky: #dcecfb;
    --stripe: #ececec;
    --white: #ffffff;
  }
  * { margin: 0; padding: 0; box-sizing: border-box; }
  html, body { width: 1200px; height: 433px; overflow: hidden; background: var(--white); }
  .label {
    position: relative;
    width: 1200px; height: 433px;
    background: var(--white);
    font-family: "Roboto Condensed", "Arial Narrow", sans-serif;
    overflow: hidden;
  }
  .band-top { position: absolute; left: 0; top: 0; width: 1200px; height: 12px; background: var(--orange); }
  .band-bottom { position: absolute; left: 0; bottom: 0; width: 1200px; height: 16px;
    background: linear-gradient(90deg, var(--blue), var(--teal)); }

  .heading { position: absolute; color: var(--orange); font-weight: 700; font-size: 21px; line-height: 24px; }
  .copy { position: absolute; color: var(--grey-text); font-weight: 700; font-size: 10px; line-height: 10.6px; }

  .facts-box { position: absolute; left: 62px; top: 135px; width: 278px; height: 274px;
    border: 2px solid var(--ink); border-radius: 12px; }
  .facts-rule { position: absolute; left: 70px; width: 256px; height: 4px; background: var(--blue); }
  .facts-row { position: absolute; left: 72px; width: 236px; color: var(--grey-text);
    font-weight: 700; font-size: 10px; display: flex; white-space: nowrap; }
  .facts-row .dots { flex: 1; overflow: hidden; }

  .front { position: absolute; left: 400px; top: 12px; width: 412px; height: 405px; overflow: hidden; }
  .front-backdrop { position: absolute; inset: 0;
    background: radial-gradient(ellipse at 20% 70%, #bcdcf6 0%, var(--panel-sky) 35%, #f7fbff 70%, var(--white) 100%); }
  .brand { position: absolute; left: 22px; top: 38px; display: flex; align-items: center; gap: 8px;
    font-family: "Roboto", sans-serif; font-weight: 700; font-size: 24px; color: var(--blue); letter-spacing: 1px; }
  .brand-dot { width: 14px; height: 14px; border-radius: 50%; background: var(--teal); }
  .tag { position: absolute; left: 328px; top: 40px; width: 72px; height: 20px; background: var(--orange); }
  .product-oval { position: absolute; left: 0; top: 0; }
  .product-name { position: absolute; left: 80px; top: 146px; color: var(--white); font-weight: 700; font-size: 25px; line-height: 30px; }
  .product-sub { position: absolute; right: 84px; top: 176px; color: var(--white); font-weight: 700; font-size: 19px; line-height: 24px; }
  .benefits { position: absolute; left: 112px; top: 286px; list-style: none;
    font-family: "Roboto", sans-serif; font-size: 11.5px; color: var(--green); }
  .benefits li { height: 19.5px; display: flex; align-items: center; gap: 7px; }
  .benefits li::before { content: ""; width: 6px; height: 6px; background: var(--green); }
  .front-footer { position: absolute; left: 0; top: 358px; width: 412px; height: 47px; background: var(--stripe); }
  .daily { position: absolute; left: 0; top: 364px; width: 412px; text-align: center;
    font-family: "Roboto", sans-serif; font-weight: 500; font-size: 12.5px; color: var(--green); }
  .daily-rule { position: absolute; left: 123px; top: 382px; width: 154px; height: 2px; background: var(--green); }
  .pack-info { position: absolute; left: 0; top: 388px; width: 412px; text-align: center;
    font-family: "Roboto", sans-serif; font-size: 7.5px; color: #555; letter-spacing: 0.3px; }
</style>
</head>
<body>
<div class="label">
  <div class="band-top"></div>

  <!-- Left side panel -->
  <h2 class="heading" style="left:71px; top:21px;">Metabolism</h2>
  <p class="copy" style="left:71px; top:47px; width:265px;">The lorem ispum text is dummy text for printing and web. This is made by our official website. We can show different text according to our use .The lorem ispum text is dummy text for printing and web. This is made by our official website. We can show different text according to our use .The lorem ispum text is dummy text for printing and web. This is made by our official website. We can show different text according to our use .</p>

  <div class="facts-box"></div>
  <h2 class="heading" style="left:71px; top:140px;">Metabolism</h2>
  <div class="facts-rule" style="top:163px;"></div>
  <div class="facts-row" style="top:172px;"><span>The lorem ispum text is dummy</span><span class="dots">..............................................</span><span>100mg</span></div>
  <div class="facts-rule" style="top:187px;"></div>
  <div class="facts-row" style="top:196px;"><span>The lorem ispum text is dummy</span><span class="dots">..............................................</span><span>100mg</span></div>
  <div class="facts-rule" style="top:212px;"></div>
  <div class="facts-row" style="top:221px;"><span>The lorem ispum text is dummy</span><span class="dots">..............................................</span><span>100mg</span></div>
  <div class="facts-rule" style="top:236px;"></div>
  <div class="facts-row" style="top:245px;"><span>The lorem ispum text is dummy</span><span class="dots">..............................................</span><span>100mg</span></div>
  <p class="copy" style="left:71px; top:264px; width:262px;">The lorem ispum text is dummy text for printing and web. This is made by our official website. We can show different text according to our use .The lorem ispum text is dummy text for printing and web. This is made by our official website. We can show different text according to our use .The lorem ispum text is dummy text for printing and web. This is made by our official website. We can show different text according to our use .The lorem ispum text is dummy text for printing and web. This is made by our official website. We can show different text according to our use .The lorem ispum text is dummy text for printing and web. This is made by our official website. We can show different text according to our use .</p>

  <!-- Front panel -->
  <div class="front">
    <div class="front-backdrop" role="img" aria-label="Soft blue flowing wave background"></div>
    <div class="brand"><span class="brand-dot"></span><span>VELUNOR</span></div>
    <div class="tag"></div>
    <svg class="product-oval" width="412" height="405" viewBox="0 0 412 405" aria-hidden="true">
      <ellipse cx="208" cy="176" rx="188" ry="64" transform="rotate(-9 208 176)" fill="#ef6748"/>
    </svg>
    <div class="product-name">Multivitamins &amp; Minerals</div>
    <div class="product-sub">Health Fitness</div>
    <ul class="benefits">
      <li>Healthy Energy Levels</li>
      <li>Healthy Immune System Function</li>
      <li>Healthy Maetabolism</li>
    </ul>
    <div class="front-footer" role="img" aria-label="Light grey diagonal stripe texture"></div>
    <div class="daily">DAILY NUTRITION</div>
    <div class="daily-rule"></div>
    <div class="pack-info">60 CAPSULES &nbsp;|&nbsp; DIETRY SUPPLEMENT</div>
  </div>

  <!-- Right side panel -->
  <h2 class="heading" style="left:872px; top:21px;">How to use it.</h2>
  <p class="copy" style="left:872px; top:49px; width:262px;">The lorem ispum text is dummy text for printing and web. This is made by our official website. We can show different text according to our use .The lorem ispum text is dummy text for printing and web. This is made by our official website. We can show different text according to our use .The lorem ispum text is dummy text for printing and web. This is made by our official website. We can show different text according to our use .</p>

  <h2 class="heading" style="left:872px; top:155px;">Precautions</h2>
  <p class="copy" style="left:872px; top:182px; width:262px;">The lorem ispum text is dummy text for printing and web. This is made by our official website. We can show different text according to our use .The lorem ispum text is dummy text for printing and web. This is made by our official website. We can show different text according to our use .The lorem ispum text is dummy text for printing and web. This is made by our official website. We can show different text according to our use .</p>

  <h2 class="heading" style="left:872px; top:289px;">Safety Temperature</h2>
  <p class="copy" style="left:872px; top:316px; width:262px;">The lorem ispum text is dummy text for printing and web. This is made by our official website. We can show different text according to our use .The lorem ispum text is dummy text for printing and web. This is made by our official website. We can show different text according to our use .The lorem ispum text is dummy text for printing and web. This is made by our official website. We can show different text according to our use .</p>

  <div class="band-bottom"></div>
</div>
</body>
</html>
```